Small Catering Menu

I am looking to make a small menu for catering for my company. I am thinking of a small A5 size booklet which will also have some pictures and the cover needs to be attractive.
Likely to be 8-12 pages depending upon your design (could be less or more). I need 2-3 pages as proposal concept (Cover, inside first page and one menu page) and if we like it we will make the project guaranteed before finishing the rest of the project to add security for the designer.
Pictures will be provided to the designer whose concept is the best as they are too heavy. But use generic photos for now (rather large ones) if possible.
Logo is available and so is the inside text as well as some other tidbits.
I will provide the fonts too to ensure it maintains the corporate integrity that we are following.
Industry/Entity Type
Catering

```html
<!DOCTYPE html>
<html lang="en">
<head>
<meta charset="utf-8">
<title>Catering Menu – By the Sea &amp; Far Eastern</title>
<link rel="stylesheet" href="https://fonts.googleapis.com/css2?family=Varela+Round&family=Source+Sans+3:wght@300;400;600;700&display=swap">
<style>
  :root{
    --sea:#0f9ea6;
    --sea-light:#1eb3b8;
    --sea-dark:#0a8790;
    --sea-title:#179fa7;
    --east:#7e0d1d;
    --east-light:#98182a;
    --east-dark:#5e0713;
    --east-title:#6e0812;
    --orange:#f7a24b;
    --teal-head:#27b8b2;
    --text:#ffffff;
    --note:#d9f1f2;
  }
  *{margin:0;padding:0;box-sizing:border-box}
  html,body{width:1200px;height:423px;overflow:hidden;background:#fff}
  .spread{position:relative;width:1200px;height:423px;font-family:"Source Sans 3",sans-serif;color:var(--text)}
  .page{position:absolute;top:0;width:600px;height:423px;overflow:hidden}
  .page--sea{left:0}
  .page--east{left:600px;border-left:1px solid #ffffff55}
  .photo{position:absolute;left:0;width:600px}
  .photo--top{top:0;height:121px}
  .photo--bottom{top:348px;height:75px}
  .page--sea .photo--top{background:linear-gradient(100deg,#f3b07a 0%,#ef8a4c 25%,#f6e6c9 45%,#e8753a 65%,#f1c79d 85%,#e9a36b 100%)}
  .page--sea .photo--bottom{background:linear-gradient(90deg,#5b6a2e 0%,#2f3521 30%,#8d8c6a 55%,#c8c6b0 80%,#e5e2d0 100%)}
  .page--east .photo--top{background:linear-gradient(100deg,#f2eeea 0%,#d4294a 25%,#f7f4f2 45%,#c4cbd6 60%,#2f3b6b 75%,#b83a5a 100%)}
  .page--east .photo--bottom{background:linear-gradient(90deg,#e4c23b 0%,#e84a2a 25%,#bcd35a 45%,#f2e6c8 65%,#e9a27a 85%,#f4efe4 100%)}
  .panel{position:absolute;left:0;top:121px;width:600px;height:227px}
  .panel svg{position:absolute;inset:0}
  .title{position:absolute;font-family:"Varela Round",sans-serif;font-size:64px;line-height:1;letter-spacing:.5px;white-space:nowrap}
  .page--sea .title{left:48px;top:52px;color:var(--sea-title)}
  .page--east .title{left:215px;top:56px;color:var(--east-title)}
  .note{position:absolute;font-size:8px;font-weight:300;color:var(--note);white-space:nowrap}
  .col{position:absolute}
  .group{margin-bottom:7px}
  .group h3{font-size:16px;font-weight:700;line-height:18px;letter-spacing:.1px}
  .group p{font-size:10.5px;font-weight:300;line-height:12px;white-space:nowrap}
  .page--sea h3{color:var(--orange)}
  .page--east h3{color:var(--teal-head)}
  .surcharge{position:absolute;font-size:8px;font-weight:300;line-height:11px;color:var(--orange)}
</style>
</head>
<body>
<div class="spread">

  <section class="page page--sea">
    <div class="photo photo--top" role="img" aria-label="Photo of salmon sushi rolls topped with salmon roe and lime"></div>
    <div class="panel">
      <svg width="600" height="227" viewBox="0 0 600 227" aria-hidden="true">
        <rect width="600" height="227" fill="var(--sea)"/>
        <polygon points="0,0 300,113 0,227" fill="var(--sea-dark)" opacity=".55"/>
        <polygon points="600,0 300,113 600,227" fill="var(--sea-light)" opacity=".6"/>
        <polygon points="120,0 480,0 300,113" fill="var(--sea-light)" opacity=".35"/>
      </svg>
      <p class="note" style="left:336px;top:10px">Choose one item from each category.&nbsp; Pricing is OMR 4.5 per person</p>
      <div class="col" style="left:46px;top:23px">
        <div class="group"><h3>Appetizers</h3><p>Dynamite Shrimps</p><p>Tuna Fish Cutlets</p></div>
        <div class="group"><h3>Sandwiches</h3><p>Tuna Sandwich</p><p>Pan Fried Baja Fish Fillet in Ciabatta Bread with Cheese</p></div>
        <div class="group"><h3>Salads</h3><p>Salmon and Green Mango Salad with Thai Dressing</p><p>Calamari and Mandarin Salad with Ginger Dressing</p></div>
        <div class="group"><h3>Soups</h3><p>Tom Yum Soup</p><p>Spicy Seafood Soup</p></div>
      </div>
      <div class="col" style="left:306px;top:23px">
        <div class="group"><h3>Main Courses</h3><p>Seared Salmon “White Rice or Pilao Rice”</p><p>Calamari in Black Pepper Sauce “White Rice or Pilao Rice”</p></div>
        <div class="group"><h3>Desserts</h3><p>Tiramisu</p><p>Fruit Salad</p></div>
        <div class="group"><h3>Drinks</h3><p>Sodas “Fizzco Brand” or Water</p><p>Choice of Fresh Juices</p><p>Lemon Mint</p><p>Iced Tea</p></div>
      </div>
      <p class="surcharge" style="left:306px;top:198px;width:240px">An Additional 10% for replacement of every item on the menu with an other from outside the menu (per head)</p>
    </div>
    <div class="photo photo--bottom" role="img" aria-label="Photo of steamed mussels with herbs"></div>
    <h1 class="title">By the Sea</h1>
  </section>

  <section class="page page--east">
    <div class="photo photo--top" role="img" aria-label="Photo of yogurt parfait cups topped with raspberries and blueberries"></div>
    <div class="panel">
      <svg width="600" height="227" viewBox="0 0 600 227" aria-hidden="true">
        <rect width="600" height="227" fill="var(--east)"/>
        <polygon points="0,0 300,113 0,227" fill="var(--east-light)" opacity=".9"/>
        <polygon points="600,0 300,113 600,227" fill="var(--east-dark)" opacity=".7"/>
        <polygon points="120,227 480,227 300,113" fill="var(--east-dark)" opacity=".35"/>
      </svg>
      <p class="note" style="left:341px;top:10px">Choose one item from each category.&nbsp; Pricing is OMR 4 per person</p>
      <div class="col" style="left:46px;top:28px">
        <div class="group"><h3>Appetizers</h3><p>Prawn Wasabi Mayo</p><p>Chicken Satay</p></div>
        <div class="group"><h3>Sandwiches</h3><p>Katsu Sando (Chicken Cutlets)</p><p>Banhmi (Vietnamese Sandwich)</p></div>
        <div class="group"><h3>Salads</h3><p>Breaded Chicken and Mandarin Salad</p><p>Thai Beef Salad with Thai Chili Dressing</p></div>
      </div>
      <div class="col" style="left:220px;top:28px">
        <div class="group"><h3>Soups</h3><p>Wonton Soup</p><p>Tom Yum Soup</p></div>
        <div class="group"><h3>Main Courses</h3><p>Black Peppered Beef with “White Rice</p><p>or Egg Fried Rice”</p><p>Thai Chicken with Cashew Nuts&nbsp; with</p><p>“White Rice or Egg Fried Rice”</p></div>
        <div class="group"><h3>Desserts</h3><p>Thai Mango Cheesecake</p><p>Asian Fruit Salad</p></div>
      </div>
      <div class="col" style="left:393px;top:28px">
        <div class="group"><h3>Drinks</h3><p>Sodas “Fizzco Brand” or Water</p><p>Choice of Fresh Juice</p><p>Lemon Mint</p><p>Iced Tea</p></div>
      </div>
      <p class="surcharge" style="left:347px;top:196px;width:225px">An Additional 10% for replacement of every item on the menu with another from outside the menu (per head)</p>
    </div>
    <div class="photo photo--bottom" role="img" aria-label="Photo of colourful Asian salad with peppers and seafood"></div>
    <h1 class="title">Far Eastern</h1>
  </section>

</div>
</body>
</html>
```